2 Creative Website Banners for Furniture Brand

Morning Tobrasca....
The get a great night sleep banner is complete - we are happy with that one.
Ive uploaded a slightly different concept for the other banner below. This is just something rough ive thrown together. But you can see I have added a curve, a maroon coloured background which is slightly transparent and a big heart in the background....
I do not necessarily want to use this heart image but something a bit like this (a nice graphic, gif etc) but something quite elegant faded in, or perhaps a number of hearts (done in a tasteful way). Also can we keep the typography in the same format as you can see for this one.
Nearly there :)!
Industry/Entity Type
Furniture

```html
<!DOCTYPE html>
<html lang="en">
<head>
<meta charset="utf-8">
<title>Find a Look You Love — Banner</title>
<link rel="stylesheet" href="https://fonts.googleapis.com/css2?family=Bodoni+Moda:wght@600&family=Lato:wght@400&family=Noto+Serif:wght@700&display=swap">
<style>
  :root {
    --ink-dark: #121214;
    --ink-mid: #25252a;
    --mauve-dark: #4e4650;
    --mauve-mid: #776c78;
    --mauve-light: #9a8f98;
    --maroon-veil: rgba(96, 14, 40, 0.58);
    --maroon-edge: rgba(236, 19, 128, 0.55);
    --heart-fill: rgba(255, 255, 255, 0.05);
    --heart-line: rgba(236, 19, 128, 0.22);
    --white: #ffffff;
    --love-pink: #ec1380;
  }
  * { margin: 0; padding: 0; box-sizing: border-box; }
  html, body {
    width: 1200px;
    height: 356px;
    overflow: hidden;
    background: var(--ink-dark);
  }
  .banner {
    position: relative;
    width: 1200px;
    height: 356px;
    overflow: hidden;
  }
  .scene-dressing {
    position: absolute;
    top: 0;
    left: 0;
    width: 623px;
    height: 356px;
    background:
      radial-gradient(ellipse at 70% 40%, rgba(70, 70, 78, 0.55), transparent 60%),
      linear-gradient(180deg, var(--ink-mid) 0%, var(--ink-dark) 100%);
  }
  .scene-bedroom {
    position: absolute;
    top: 0;
    left: 623px;
    width: 577px;
    height: 356px;
    background:
      radial-gradient(ellipse at 40% 65%, rgba(185, 175, 185, 0.55), transparent 55%),
      linear-gradient(135deg, var(--mauve-dark) 0%, var(--mauve-mid) 55%, var(--mauve-light) 100%);
  }
  .veil {
    position: absolute;
    inset: 0;
    width: 1200px;
    height: 356px;
  }
  .veil-shape { fill: var(--maroon-veil); }
  .veil-edge { fill: none; stroke: var(--maroon-edge); stroke-width: 2; }
  .heart { fill: var(--heart-fill); stroke: var(--heart-line); stroke-width: 1.2; }
  .headline {
    position: absolute;
    left: 60px;
    top: 0;
    width: 508px;
    height: 356px;
    color: var(--white);
    text-align: center;
  }
  .headline-kicker {
    position: absolute;
    left: 0;
    right: 0;
    top: 44px;
    font-family: "Lato", sans-serif;
    font-weight: 400;
    font-size: 39px;
    line-height: 48px;
    letter-spacing: 0.27em;
    text-indent: 0.27em;
    white-space: nowrap;
  }
  .headline-love {
    position: absolute;
    left: 11px;
    right: 11px;
    top: 98px;
    display: flex;
    justify-content: space-between;
    font-family: "Bodoni Moda", serif;
    font-weight: 600;
    font-size: 99px;
    line-height: 104px;
    color: var(--love-pink);
  }
  .headline-sub {
    position: absolute;
    left: 0;
    right: 0;
    top: 210px;
    font-family: "Noto Serif", serif;
    font-weight: 700;
    font-size: 20px;
    line-height: 29px;
    letter-spacing: 0.1em;
    white-space: nowrap;
  }
</style>
</head>
<body>
  <main class="banner">
    <div class="scene-dressing" role="img" aria-label="Dark boudoir with a mirrored dressing table, glass jars, orchids and a velvet stool"></div>
    <div class="scene-bedroom" role="img" aria-label="Bedroom in mauve and grey with an upholstered bed, faux fur throw, mirrored bedside tables and lamp"></div>

    <svg class="veil" viewBox="0 0 1200 356" aria-hidden="true">
      <defs>
        <symbol id="heart-shape" viewBox="0 0 100 88">
          <path d="M50 86 C20 62 2 46 2 25 C2 11 13 2 27 2 C38 2 46 9 50 17 C54 9 62 2 73 2 C87 2 98 11 98 25 C98 46 80 62 50 86Z"/>
        </symbol>
      </defs>
      <path class="veil-shape" d="M0 0 H640 C700 110 690 250 600 356 H0 Z"/>
      <path class="veil-edge" d="M640 0 C700 110 690 250 600 356"/>
      <use class="heart" href="#heart-shape" x="170" y="30" width="300" height="264"/>
      <use class="heart" href="#heart-shape" x="18" y="250" width="70" height="62"/>
      <use class="heart" href="#heart-shape" x="540" y="280" width="46" height="40"/>
      <use class="heart" href="#heart-shape" x="575" y="18" width="34" height="30"/>
    </svg>

    <section class="headline">
      <p class="headline-kicker">FIND A LOOK YOU</p>
      <h1 class="headline-love" aria-label="LOVE">
        <span>L</span><span>O</span><span>V</span><span>E</span>
      </h1>
      <p class="headline-sub">Lorem Ipsum not sure what the rest of<br>this will say at the moment</p>
    </section>
  </main>
</body>
</html>
```